Poster Needed for Church Conference

I need a poster for a weekend conference at my church. Looking to attract as many people as possible. We are a church in the suburbs of Houston. This is mainly for our own church members but we are opening it up to outside church members.

Please see previous design from last conference and all other graphic work that can (doesn't need to be) included.

Target Market(s)

It's targeted for all people. But our main audience is families. around the age of 30 should be main target.

Industry/Entity Type

Non-Profit

Font styles to use
Serif
Sans Serif

Colors

Designer to choose colors to be used in the design.

Requirements
Must have
• 11x17 design with ability to shrink and blow up. but ideally for 11x17
• Content and wording:
• "Rooted Light Conference: Bridging the gap between generations and passing on our deepest beliefs and values."
• Featuring Dr. Gil Marsden. Author of "The Path of P4"
• Aug 25-26: Friday 8-10 pm, Saturday 4-8 pm
• Cost Adults $15/Children $5: Covers admission to all sessions and workshops, refreshments and Saturday dinner. *kids 5 and under free
• Childcare provided for all sessions. "
• Please use church logo and address on flyer: 4312 Route 19, Missouri City, TX 77988
Nice to have
• Ideally it will be designed so that we can crop a 16:9 pp announcement slide and header for our website.
Should not have
• anything offensive

```html
<!DOCTYPE html>
<html lang="en">
<head>
<meta charset="utf-8">
<title>Rooted Light Conference Poster</title>
<link rel="stylesheet" href="https://fonts.googleapis.com/css2?family=Josefin+Sans:wght@400;600;700&display=swap">
<style>
  :root {
    --backdrop: #e4e4e4;
    --paper: #ffffff;
    --ray: #f3f3f3;
    --yellow: #fff200;
    --blue: #1daee6;
    --green: #5cbc0c;
    --green-line: #5cc21a;
    --white: #ffffff;
    --grey-edge: #d9d9d9;
    --photo: #6b5a4e;
    --book: #dfe8e2;
  }
  * { margin: 0; padding: 0; box-sizing: border-box; }
  html, body {
    width: 1200px; height: 798px; overflow: hidden;
    background: var(--backdrop);
    font-family: "Josefin Sans", sans-serif;
  }
  .poster {
    position: absolute; left: 363px; top: 33px;
    width: 474px; height: 731px; overflow: hidden;
    background:
      repeating-conic-gradient(from 0deg at 50% 62%, var(--ray) 0deg 5deg, var(--paper) 5deg 10deg);
  }
  .shapes { position: absolute; inset: 0; }
  .text { position: absolute; font-variant: small-caps; line-height: 1; }

  .title {
    left: 0; width: 474px; top: 118px; text-align: center;
    font-weight: 700; font-size: 47px; letter-spacing: -2.5px;
    color: var(--blue); font-variant: normal; text-transform: uppercase;
    line-height: 48px;
    text-shadow: -3px 3px 0 var(--white);
  }
  .tagline {
    left: 0; width: 484px; top: 222px; text-align: center;
    font-size: 14px; letter-spacing: 0.8px; line-height: 13px;
    color: var(--blue);
  }
  .featuring { left: 237px; top: 355px; font-size: 15px; color: var(--yellow); }
  .speaker { left: 237px; top: 383px; font-size: 16px; color: var(--yellow); }
  .author-of { left: 237px; top: 397px; font-size: 12px; color: var(--yellow); }
  .book-title { left: 237px; top: 410px; font-size: 16px; color: var(--white); }

  .when-heading { right: 260px; top: 406px; font-size: 21px; color: var(--green); font-variant: normal; text-transform: uppercase; font-weight: 400; }
  .when-dates { right: 260px; top: 439px; font-size: 10px; line-height: 12px; color: var(--green); text-align: right; font-variant: normal; text-transform: uppercase; }

  .cost-heading { left: 232px; top: 466px; font-size: 13.5px; color: var(--white); }
  .cost-details { left: 232px; top: 488px; width: 170px; font-size: 8.6px; line-height: 10.8px; color: var(--white); }

  .church-name {
    left: 0; width: 474px; top: 583px; text-align: center;
    color: var(--green); font-weight: 400; font-variant: normal;
  }
  .church-name .mark {
    display: inline-block; width: 20px; height: 20px; border-radius: 50%;
    background: var(--green); vertical-align: -3px; margin-right: 8px;
  }
  .church-name .name { font-size: 22px; letter-spacing: 0.5px; }
  .church-rule { position: absolute; left: 143px; top: 629px; width: 184px; height: 1px; background: var(--green); }
  .address { left: 0; width: 474px; top: 640px; text-align: center; font-size: 11px; line-height: 13px; color: var(--green); }
</style>
</head>
<body>
  <main class="poster">
    <svg class="shapes" width="474" height="731" viewBox="0 0 474 731">
      <!-- outline swirls -->
      <g fill="none" stroke="var(--green-line)" stroke-width="1">
        <path d="M60 140 C20 200, 30 300, 120 320 C200 340, 240 330, 258 400"/>
        <path d="M90 110 C10 160, 0 290, 90 330 C170 360, 230 350, 250 405"/>
        <path d="M400 100 C470 150, 480 260, 410 300 C350 330, 300 320, 275 370"/>
        <path d="M430 130 C490 220, 460 300, 380 320 C320 335, 290 340, 270 380"/>
        <path d="M140 75 C60 100, 40 170, 70 230 C110 300, 230 290, 255 360"/>
      </g>
      <!-- headline bubble -->
      <path fill="var(--blue)" d="M112 88 C212 63 372 68 422 118 C452 158 447 258 392 283 C342 306 292 298 272 308 C262 318 258 330 262 345 C248 318 232 306 192 300 C112 298 37 283 32 208 C27 138 52 103 112 88 Z"/>
      <path fill="var(--yellow)" d="M120 80 C220 55 380 60 430 110 C460 150 455 250 400 275 C350 298 300 290 280 300 C268 310 264 322 262 335 C255 310 240 298 200 292 C120 290 45 275 40 200 C35 130 60 95 120 80 Z"/>
      <!-- when bubble -->
      <path fill="var(--grey-edge)" d="M226 492 C214 474 196 474 166 474 L76 474 Q41 474 41 432 Q41 378 94 378 L226 378 Z"/>
      <path fill="var(--white)" d="M223 487 C210 470 190 470 160 470 L72 470 Q37 470 37 430 Q37 374 90 374 L223 374 Z"/>
      <!-- featuring bubble -->
      <path fill="var(--green)" d="M223 338 Q223 318 243 318 L418 318 Q438 318 438 338 L438 425 Q438 443 418 443 L223 443 Z"/>
      <!-- cost bubble -->
      <path fill="var(--blue)" d="M223 440 L395 440 Q415 440 415 460 L415 520 Q415 548 385 548 L265 548 Q235 548 226 590 L223 597 Z"/>
      <!-- speaker photo and book -->
      <circle cx="409" cy="345" r="33" fill="var(--yellow)"/>
      <circle cx="409" cy="345" r="30" fill="var(--photo)" role="img" aria-label="Portrait photo of the featured speaker"/>
      <circle cx="395" cy="399" r="33" fill="var(--yellow)"/>
      <circle cx="395" cy="399" r="30" fill="var(--book)" role="img" aria-label="Cover of the speaker's book"/>
    </svg>

    <h1 class="text title">Rooted Light<br>Conference</h1>
    <p class="text tagline">Bridging the gap between generations and<br>passing on our deepest beliefs and values.</p>

    <p class="text featuring">Featuring</p>
    <p class="text speaker">Dr. Gil Marsden.</p>
    <p class="text author-of">Author of</p>
    <p class="text book-title">"The Path of P4"</p>

    <p class="text when-heading">When?</p>
    <p class="text when-dates">August 25 | Friday | 8:00-10:00pm<br>August 26 | Saturday | 4:00-8:00pm</p>

    <p class="text cost-heading">Cost Adults $15/Children $5</p>
    <p class="text cost-details">Covers admission to all sessions and workshops, refreshments and Saturday dinner.<br>*kids 5 and under free*<br>Childcare provided for all sessions.</p>

    <p class="text church-name"><span class="mark"></span><span class="name">Oak Hollow Community Church</span></p>
    <div class="church-rule"></div>
    <p class="text address">4312 Route 19, Missouri<br>City, TX 77988</p>
  </main>
</body>
</html>
```